Pennavora Web Design Project

We will need only one logo for Pennavora
Front Page
Header - Pennavora (logo) - Sites - Categories - Featured Contributors - Login (end header - the way plotharbor does this is great, but I'm open to new ideas also)
(Start Page Content)
Pennavora (logo - centered)
quirkyhourly.com - thezephant.com - stokingmoss.com (please leave spaces where we can place screenshots of those pages)
Sign Up!
Pennavora is a constantly growing network of sites that are dedicated to create relevant and well written content. If you are a student, professional, or a retiree, and you have an idea about a website that you would like to Contribute to, then this is the community that you have been looking for.
How It Works
Contribute An Article - Get Published - Increase Your Digital Footprint
Why We Exist
In the days when newspapers and radio stations dictated what the public read and heard, writers and editors were the gatekeepers in front of knowledge.
Those days are over and the lines between people who read content and publish content have become blurred. The outer-space like vastness of the internet is made larger exponentially every second by people who contribute data to it.
We believe that the future of knowledge in this world will have no gatekeepers and that every person is a contributor. This belief has lead to the creation of Pennavora.
Pennavora (logo-centered) - By The People, For The People
Footer
Follow Us: facebook, twitter, google+, youtube, instagram, linked in
____________________________
Categories Page (will need it's own page)
Arts & Entertainment - quirkyhourly.com
Health & Fitness - stokingmoss.com
News - thezephant.com
If you’re interested in contributing to a topic listed below please email us at info@pennavora.com
Automotive
Business
Careers
Education
Family & Parenting
Personal Finance
Food & Drink
Hobbies & Interests
Home & Garden
Law, Government & Politics
Society
Science
Pets
Sports
Style & Fashion
Technology & Computing
Travel
Real Estate
Shopping
Religion and Spirituality
Uncategorized
___________________________
Sites Page (will need it's own page)
Quirky Hourly - quirkyhourly.com is an Arts & Entertainment website consisting of photo galleries and descriptions.
The Zephant - thezephant.com is a News website that is specifically dedicated to newly trending topics.
Stoking Moss - stokingmoss.com is a Health & Fitness website where visitors can find articles about workout routines, health supplements, and get ideas for eating clean.
_________________________
Featured Contributors Page (will need it's own page)
Content is to be determined
__________________________
NOTES FOR DESIGNER
We also will need a two column sub page that with one column being thin for navigation. We really like the simplicity of tidleno.com and plotharbor.com. Those are two sites you can reference for the direcion we are heading in.
Thanks!
-Corey
Updates
Hey Everyone!

```html
<!DOCTYPE html>
<html lang="en">
<head>
<meta charset="utf-8">
<title>Pennavora</title>
<link rel="stylesheet" href="https://fonts.googleapis.com/css2?family=PT+Sans:wght@400;700&family=Arimo:wght@400;700&display=swap">
<style>
:root{
  --blue:#1592cf;
  --blue-deep:#0f8ccb;
  --teal:#4ab5b1;
  --band:#e6e6e6;
  --rule:#c9c9c9;
  --field:#cfe4f1;
  --field-border:#8cc3e3;
  --field-text:#1a5f87;
  --ink:#555;
  --white:#fff;
}
*{box-sizing:border-box;margin:0;padding:0}
html,body{width:1166px;height:1200px;overflow:hidden;background:var(--white)}
body{position:relative;font-family:"Arimo",Arial,sans-serif;color:var(--ink)}

.site-header{position:absolute;left:0;top:0;width:1166px;height:105px;border-bottom:5px solid var(--rule);height:110px}
.brand{position:absolute;left:42px;top:38px;display:flex;align-items:center;gap:8px}
.brand-dot{width:26px;height:26px;border-radius:50%;background:var(--blue)}
.brand-name{font-family:"PT Sans",sans-serif;font-weight:700;font-size:21px;color:var(--teal)}
.main-nav{position:absolute;left:180px;top:43px;display:flex;gap:46px}
.main-nav a{font-family:"PT Sans",sans-serif;font-size:20px;color:var(--blue);text-decoration:none}
.account{position:absolute;left:921px;top:0;width:186px;height:86px;display:flex;border-radius:0 0 5px 5px;overflow:hidden}
.account a{flex:1;display:flex;flex-direction:column;align-items:center;justify-content:flex-end;padding-bottom:8px;color:var(--white);font-size:13px;text-decoration:none}
.account .signup{background:var(--blue)}
.account .login{background:var(--teal)}
.account svg{margin-bottom:6px}
.account-joint{position:absolute;left:87px;top:47px;width:14px;height:14px;border-radius:50%;background:#2b5c9c;border:2px solid #9bc7e3}

.showcase{position:absolute;left:0;top:110px;width:1166px;height:259px;background:var(--band)}
.arrow{position:absolute;top:86px}
.arrow.prev{left:18px}
.arrow.next{right:18px}
.site-card{position:absolute;top:38px;width:245px;text-align:center}
.site-shot{width:245px;height:156px;border:6px solid #aaa;background:linear-gradient(#fafafa,#e9e9e9)}
.site-card h3{margin-top:8px;font-weight:400;font-size:16px;color:#444}
.site-card p{font-size:12px;color:#888;margin-top:2px}

.intro{position:absolute;left:0;top:369px;width:1166px;height:446px;background:var(--blue-deep);color:var(--white)}
.signup-form{position:absolute;left:18px;top:0;width:372px}
.signup-form h2{font-family:"PT Sans",sans-serif;font-size:41px;font-weight:400;margin-top:28px;margin-left:2px}
.field{position:absolute;height:31px;background:var(--field);border:1px solid var(--field-border);border-radius:3px;padding:6px 10px;font-size:14px;font-weight:700;color:var(--field-text)}
.row-label{position:absolute;left:3px;font-size:15px;font-weight:700;color:#d8ecf8}
.radio{position:absolute;top:248px;font-size:12px;color:#d8ecf8;display:flex;align-items:center;gap:6px}
.radio i{width:13px;height:13px;border-radius:50%;background:#e3eef5;border:1px solid #9bbfd6}
.select{position:absolute;top:272px;height:30px;background:var(--field);border:1px solid var(--field-border);border-radius:3px;font-size:14px;font-weight:700;color:var(--field-text);padding:6px 10px}
.select b{position:absolute;right:4px;top:5px;width:18px;height:18px;border:1px solid #555;background:#ddd}
.select b::after{content:"";position:absolute;left:4px;top:6px;border:4px solid transparent;border-top:6px solid #222}
.terms{position:absolute;left:2px;top:318px;width:372px;font-size:12.5px;line-height:1.3;color:#e6f3fb}
.terms strong{color:var(--white)}
.signup-btn{position:absolute;left:-1px;top:376px;width:96px;height:39px;border-radius:3px;background:linear-gradient(#7fcaf0,#3aa5dc);border:1px solid #a8daf3;color:var(--white);font-size:14px;font-weight:700;text-align:center;line-height:37px}
.signin{position:absolute;left:108px;top:388px;font-size:14px;font-weight:700;color:#d8ecf8}
.signin strong{color:var(--white)}

.about{position:absolute;left:439px;top:0;width:690px}
.about h2{font-family:"PT Sans",sans-serif;font-weight:700;font-size:26px;line-height:1}
.about .lead{font-size:16px;line-height:1.22;margin-top:6px}
.about .steps{font-family:"PT Sans",sans-serif;font-size:20px;color:#dbeef8;margin-top:6px}
.about .small{font-size:13.5px;line-height:1.22;margin-top:7px}
.block-what{position:absolute;top:35px}
.block-how{position:absolute;top:175px}
.block-why{position:absolute;top:266px}

.closing{position:absolute;left:0;top:862px;width:1166px;text-align:center}
.closing .mark{display:inline-flex;align-items:center;gap:14px}
.closing .mark i{width:62px;height:62px;border-radius:50%;background:var(--blue)}
.closing .mark span{font-family:"PT Sans",sans-serif;font-weight:700;font-size:48px;color:var(--teal)}
.tagline{font-family:"PT Sans",sans-serif;font-weight:700;font-size:56px;margin-top:48px;color:var(--blue)}
.tagline em{font-style:normal;color:var(--teal)}

.site-footer .follow{position:absolute;left:26px;top:1120px;font-size:16px;color:#666}
.social{position:absolute;left:24px;top:1146px;display:flex;gap:9px}
.social a{width:36px;height:36px;border-radius:4px;border:1px solid #9aa;background:linear-gradient(#f2f2f2,#cfd6da)}
.copyright{position:absolute;right:20px;top:1162px;font-size:14px;color:#666}
</style>
</head>
<body>

<header class="site-header">
  <div class="brand"><span class="brand-dot"></span><span class="brand-name">Pennavora</span></div>
  <nav class="main-nav">
    <a href="#">Sites</a><a href="#">Categories</a><a href="#">Featured</a><a href="#">Contributors</a>
  </nav>
  <div class="account">
    <a class="signup" href="#">
      <svg width="36" height="40" viewBox="0 0 36 40" fill="none" stroke="#fff" stroke-width="2.5"><path d="M4 3h18l8 8v26H4z"/><path d="M10 15h14M10 21h14M10 27h9"/><path d="M24 36l9-13 3 2-9 13-4 1z" fill="#1592cf"/></svg>
      signup
    </a>
    <a class="login" href="#">
      <svg width="36" height="40" viewBox="0 0 36 40" fill="none" stroke="#fff" stroke-width="2.5"><path d="M4 3h18l8 8v26H4z"/><path d="M9 21l5 5 9-11"/><path d="M24 36l9-13 3 2-9 13-4 1z" fill="#4ab5b1"/></svg>
      login
    </a>
    <span class="account-joint"></span>
  </div>
</header>

<section class="showcase">
  <svg class="arrow prev" width="40" height="54" viewBox="0 0 40 54"><path d="M0 27L22 0v14h18v26H22v14z" fill="#9e9e9e"/></svg>
  <div class="site-card" style="left:161px">
    <div class="site-shot" role="img" aria-label="Screenshot of quirkyhourly.com"></div>
    <h3>Arts &amp; Entertainment</h3><p>quirkyhourly.com</p>
  </div>
  <div class="site-card" style="left:458px">
    <div class="site-shot" role="img" aria-label="Screenshot of stokingmoss.com" style="background:linear-gradient(#f4f4f4 0 18%,#2f2f2f 18% 40%,#eeeeee 40%)"></div>
    <h3>Health &amp; Fitness</h3><p>stokingmoss.com</p>
  </div>
  <div class="site-card" style="left:756px">
    <div class="site-shot" role="img" aria-label="Screenshot of thezephant.com" style="background:linear-gradient(#fafafa 0 45%,#e4e4e4 45%)"></div>
    <h3>News</h3><p>thezephant.com</p>
  </div>
  <svg class="arrow next" width="40" height="54" viewBox="0 0 40 54"><path d="M40 27L18 0v14H0v26h18v14z" fill="#9e9e9e"/></svg>
</section>

<section class="intro">
  <form class="signup-form">
    <h2>Signup Now</h2>
    <div class="field" style="left:0;top:86px;width:179px">First Name</div>
    <div class="field" style="left:190px;top:86px;width:179px">Last Name</div>
    <div class="field" style="left:0;top:125px;width:369px">Your Email</div>
    <div class="field" style="left:0;top:164px;width:369px">Re-enter Email</div>
    <div class="field" style="left:0;top:203px;width:369px">Password</div>
    <span class="row-label" style="top:248px">Gender</span>
    <span class="radio" style="left:105px">female <i></i></span>
    <span class="radio" style="left:176px">female <i></i></span>
    <span class="row-label" style="top:281px">Birthday</span>
    <div class="select" style="left:101px;width:96px">Month<b></b></div>
    <div class="select" style="left:204px;width:85px">Day<b></b></div>
    <div class="select" style="left:295px;width:86px">Year<b></b></div>
    <p class="terms">By clicking Sign Up, you agree to our <strong>Terms</strong> and that you have read and understand our <strong>Data Use Policy</strong>, including our Cookie Use.</p>
    <div class="signup-btn">sign up</div>
    <p class="signin">I already have an account. <strong>Sign In</strong></p>
  </form>

  <div class="about">
    <div class="block-what">
      <h2>What is Pennavora?</h2>
      <p class="lead">Pennavora is a constantly growing network of sites that are dedicated to create relevant and well written content. If you are a student, professional, or a retiree, and you have an idea about a website that you would like to Contribute to, then this is the community that you have been looking for.</p>
    </div>
    <div class="block-how">
      <h2>How It Works?</h2>
      <p class="steps">Contribute An Article - Get Published - Increase Your Digital Footprint</p>
    </div>
    <div class="block-why">
      <h2>Why We Exist</h2>
      <p class="small">In the days when newspapers and radio stations dictated what the public read and heard, writers and editors were the gatekeepers in front of knowledge. Those days are over and the lines between people who read content and publish content have become blurred. The outer-space like vastness of the internet is made larger exponentially every second by people who contribute data to it. We believe that the future of knowledge in this world will have no gatekeepers and that every person is a contributor. This belief has lead to the creation of Pennavora.</p>
    </div>
  </div>
</section>

<section class="closing">
  <div class="mark"><i></i><span>Pennavora</span></div>
  <p class="tagline">By The People, <em>For The People</em></p>
</section>

<footer class="site-footer">
  <p class="follow">Follow Us</p>
  <div class="social">
    <a href="#" aria-label="Social profile 1"></a>
    <a href="#" aria-label="Social profile 2"></a>
    <a href="#" aria-label="Social profile 3"></a>
    <a href="#" aria-label="Social profile 4"></a>
    <a href="#" aria-label="Social profile 5"></a>
    <a href="#" aria-label="Social profile 6"></a>
  </div>
  <p class="copyright">Copyright © 2013 Pennavora. All rights reserved.</p>
</footer>

</body>
</html>
```